Snack Menu for the bowling lanes side of our business.

Build a snack menu from the appetizer and pizza portion of the menu. Some of the sandwiches could be added into this menu.
Industry/Entity Type
Business
Requirements
Must have
- Menu should be bowling themed - using bowling graphics and look different than the restaurant menu.
Nice to have
- The Copperfield Restaurant logo used on menu.

```html
<!DOCTYPE html>
<html lang="en">
<head>
<meta charset="utf-8">
<title>The Copperfield Restaurant – Snacks</title>
<link rel="stylesheet" href="https://fonts.googleapis.com/css2?family=Fira+Sans+Condensed:ital,wght@1,500;1,600&family=Tinos:wght@400;700&display=swap">
<style>
  :root {
    --brown: #3a2818;
    --brown-light: #4a3523;
    --gold: #b8950f;
    --white: #ffffff;
    --cyan: #3db4d8;
    --ink: #2b1d10;
    --pin-light: #f4f1ee;
    --pin-shade: #c9c3bd;
  }
  * { box-sizing: border-box; margin: 0; padding: 0; }
  html, body { width: 927px; height: 1200px; overflow: hidden; }
  body {
    position: relative;
    background: var(--gold);
    font-family: "Tinos", "Times New Roman", serif;
    color: var(--white);
  }
  .frame-edge {
    position: absolute; left: 0; top: 0;
    width: 927px; height: 1158px;
    background: var(--white);
    border-bottom-left-radius: 96px;
  }
  .menu-panel {
    position: absolute; left: 22px; top: 0;
    width: 905px; height: 1140px;
    background: radial-gradient(circle at 60% 45%, var(--brown-light), var(--brown) 70%);
    border-bottom-left-radius: 80px;
  }
  .left-strip {
    position: absolute; left: 0; top: 0; width: 22px; height: 600px;
    background: var(--brown);
  }
  .pin-art {
    position: absolute; left: 0; top: 0;
    width: 240px; height: 680px;
  }
  .brand {
    position: absolute; left: 330px; top: 56px; width: 270px;
    text-align: center;
    font-family: "Fira Sans Condensed", sans-serif;
    font-style: italic; font-weight: 600;
    font-size: 36px; line-height: 1.1; color: var(--white);
  }
  .brand-mark {
    display: block; width: 22px; height: 22px;
    margin: 0 auto 14px; background: var(--white);
  }
  .title-box {
    position: absolute; left: 288px; top: 258px;
    width: 256px; height: 56px;
    background: var(--white);
    display: flex; align-items: center; justify-content: center;
    font-family: "Fira Sans Condensed", sans-serif;
    font-style: italic; font-weight: 600;
    font-size: 44px; color: var(--ink);
  }
  .column { position: absolute; top: 338px; }
  .col-left { left: 144px; width: 350px; }
  .col-right { left: 520px; width: 356px; }
  .section-title {
    font-family: "Fira Sans Condensed", sans-serif;
    font-style: italic; font-weight: 500;
    font-size: 35px; line-height: 1.1;
  }
  .section-tagline {
    font-family: "Fira Sans Condensed", sans-serif;
    font-style: italic; font-weight: 600; font-size: 21px;
    margin-bottom: 10px;
  }
  .item { margin-top: 12px; }
  .col-left .section-title { margin-bottom: 4px; }
  .item-name {
    font-family: "Fira Sans Condensed", sans-serif;
    font-style: italic; font-weight: 500;
    font-size: 20px; color: var(--cyan); line-height: 1.2;
  }
  .item-desc { font-size: 17px; line-height: 1.3; }
  .price { font-weight: 700; float: right; }
  .sizes {
    display: flex; justify-content: space-between;
    font-size: 17px; line-height: 1.3;
  }
  .sizes b { font-weight: 700; }
  .col-right .item { margin-top: 6px; }
  .specials-title { margin-top: 16px; font-size: 31px; }
</style>
</head>
<body>
  <div class="frame-edge"></div>
  <div class="menu-panel"></div>
  <div class="left-strip"></div>
  <svg class="pin-art" viewBox="0 0 240 680" role="img" aria-label="Large white bowling pin with two red stripes at the neck">
    <defs>
      <linearGradient id="pinShade" x1="0" y1="0" x2="1" y2="0">
        <stop offset="0" stop-color="#c9c3bd"/>
        <stop offset="0.6" stop-color="#f4f1ee"/>
        <stop offset="1" stop-color="#cfc9c3"/>
      </linearGradient>
    </defs>
    <path d="M80 0 L230 0 C236 70 178 130 170 210 C162 290 145 330 118 400 C92 480 55 590 0 660 L0 0 Z" fill="url(#pinShade)"/>
  </svg>

  <header class="brand">
    <span class="brand-mark"></span>
    The Copperfield Restaurant
  </header>

  <div class="title-box">Snacks</div>

  <section class="column col-left">
    <h2 class="section-title">Appetizers</h2>
    <div class="item">
      <h3 class="item-name">Cheese Bread Squares</h3>
      <p class="item-desc">Copperfield original, our homemade pizza dough loaded with mozzarella cheese with a dusting of parmesan and garlic <span class="price">4.99</span></p>
    </div>
    <div class="item">
      <h3 class="item-name">Battered Mushrooms</h3>
      <p class="item-desc">Whole mushrooms battered and fried golden, served with dipping sauce <span class="price">3.99</span></p>
    </div>
    <div class="item">
      <h3 class="item-name">Battered Cauliflower</h3>
      <p class="item-desc">Cauliflower florets battered and fried golden, served with a dipping sauce <span class="price">3.99</span></p>
    </div>
    <div class="item">
      <h3 class="item-name">Cheddar Cheese Nuggets</h3>
      <p class="item-desc">Wisconsin cheddar cheese breaded and fried golden <span class="price">3.99</span></p>
    </div>
    <div class="item">
      <h3 class="item-name">Chicken Tenders</h3>
      <p class="item-desc">Tender and crispy served with your choice of dipping sauce <span class="price">4.99</span></p>
    </div>
    <div class="item">
      <h3 class="item-name">Mozzarella Sticks</h3>
      <p class="item-desc">Mozzarella cheese lightly breaded and fried, served with your choice of dipping sauce <span class="price">3.99</span></p>
    </div>
    <div class="item">
      <h3 class="item-name">Brew House Sampter</h3>
      <p class="item-desc">Beer battered favorites including chicken tenders, mushrooms, shrimp, onion rings, mozzarella cheese sticks, cream cheese stuffed peppers and Lane City fries <span class="price">6.99</span></p>
    </div>
  </section>

  <section class="column col-right">
    <h2 class="section-title">Homemade Pan Pizza</h2>
    <p class="section-tagline">Millbrook’s Finest</p>
    <div class="item">
      <h3 class="item-name">Cheese</h3>
      <p class="sizes"><span>Sm. <b>7.25</b></span><span>Med. <b>9.25</b></span><span>Lg. <b>11.25</b></span></p>
    </div>
    <div class="item">
      <h3 class="item-name">Additional Items</h3>
      <p class="sizes"><span>Sm. <b>1.25</b></span><span>Med. <b>1.50</b></span><span>Lg. <b>1.75</b></span></p>
    </div>
    <div class="item">
      <h3 class="item-name">Items:</h3>
      <p class="item-desc">Ham, Pepperoni, Hamburger, Italian Sausage, Bacon, Green Olives, Black Olives, Onions, Green Peppers, Mushrooms, Pepper Rings or Tomatoes.</p>
    </div>

    <h2 class="section-title specials-title">Copperfield Specials</h2>
    <div class="item">
      <h3 class="item-name">Copperfield Special</h3>
      <p class="item-desc">Cheese, Ham, Pepperoni, Onions, Green Peppers, Mushrooms and Italian Sausage</p>
      <p class="sizes"><span>Sm.<b>10.75</b></span><span>Med. <b>13.75</b></span><span>Lg. <b>16.50</b></span></p>
    </div>
    <div class="item">
      <h3 class="item-name">Meat Lovers</h3>
      <p class="item-desc">Cheese, ham, pepperoni, Italian sausage, bacon and beef</p>
      <p class="sizes"><span>Sm. <b>10.75</b></span><span>Med. <b>13.75</b></span><span>Lg. <b>16.50</b></span></p>
    </div>
    <div class="item">
      <h3 class="item-name">Hawaiian Pizza</h3>
      <p class="item-desc">With pineapple and ham</p>
      <p class="sizes"><span>Sm. <b>8.75</b></span><span>Med. <b>11.25</b></span><span>Lg. <b>13.75</b></span></p>
    </div>
    <div class="item">
      <h3 class="item-name">Vegetarian Pizza</h3>
      <p class="item-desc">Mushrooms, onion, tomato and green peppers</p>
      <p class="sizes"><span>Sm. <b>8.75</b></span><span>Med. <b>11.25</b></span><span>Lg. <b>13.75</b></span></p>
    </div>
    <div class="item">
      <h3 class="item-name">Personal 7" Pan Pizza</h3>
      <p class="item-desc">With any 3 items <span class="price">4.25</span></p>
    </div>
  </section>
</body>
</html>
```